Hockey Habits Poster Board for a Girls Youth Hockey Team

I'd like to have a (2) sided poster board created for our hockey team. The poster board will be 2'x4'. There are (4) different types of team play as follows:

Offense w/Puck - You have the puck and your team is on offense
-------------
Offense wo/Puck - You do not have the puck but your teammate does
-------------
Defense on/Puck - Your opponent has the puck and you are the closest defender from your team to the opponent with the puck
-------------
Defense away/Puck - Your opponent has the puck and you are not the closes defender from your team to the opponent with the puck
--------------
Individual habits are what we want every player to have regardless of the team situation. I think I'd like to have the individual habits on both sides of the poster board.

I'm open to ideas but I thought it would be cool to have a hockey rink in the background. This is also for a girls hockey team so if you are going to use a hockey player - please make sure the player is female.

Target Market(s)

Youth Hockey

Industry/Entity Type

Youth Sports - Hockey

Font styles to use
Serif
Sans Serif

Colors
0054AA
0677BA
7BADD7
CADEEF
E8F1F8
00AB8E
00BBA5
67D7C9
C6EFE9
E9F9F6

Requirements
Must have
• All of the individual habits on both sides. All the defensive habits on one side and the offensive habits on the other side.
Nice to have
• I'd like to see an image of a hockey rink on both sides of the poster as well as a female hockey player
Should not have
• boys

```html
<!DOCTYPE html>
<html lang="en">
<head>
<meta charset="utf-8">
<title>Hockey Habits</title>
<link rel="stylesheet" href="https://fonts.googleapis.com/css2?family=Russo+One&family=Roboto+Condensed:wght@300;400;700&display=swap">
<style>
:root{
  --page:#eeeeee;
  --paper:#ffffff;
  --ink:#222222;
  --red:#e05a57;
  --purple:#c45fd8;
  --blue:#4f8ede;
  --average:#ef9a97;
  --good:#f2d67a;
  --great:#a8e38a;
  --ice-dark:#0a1430;
  --ice-mid:#1f4fb0;
  --ice-light:#c9d6ea;
}
*{margin:0;padding:0;box-sizing:border-box}
html,body{width:1200px;height:2334px;overflow:hidden;background:var(--page)}
.stage{width:1324px;height:2576px;transform:scale(0.9063);transform-origin:0 0;position:relative}
.poster{position:absolute;left:45px;top:52px;width:1235px;height:2468px;background:var(--paper);box-shadow:0 0 14px rgba(0,0,0,.35);overflow:hidden;font-family:"Roboto Condensed",sans-serif;color:var(--ink)}
.hero{position:absolute;left:0;top:0;width:1235px;height:663px;
  background:
   radial-gradient(ellipse at 50% 10%,rgba(140,180,255,.55),transparent 55%),
   radial-gradient(ellipse at 15% 25%,rgba(120,160,255,.35),transparent 30%),
   linear-gradient(180deg,var(--ice-dark) 0%,var(--ice-mid) 45%,#6e8fc7 70%,var(--ice-light) 100%)}
.hero-title{position:absolute;left:0;top:0}
.tab{position:absolute;height:74px;border-radius:16px 16px 0 0;color:#fff;font-family:"Russo One",sans-serif;display:flex;align-items:center;justify-content:center;letter-spacing:1px}
.band{position:absolute;left:0;width:1235px;height:73px;color:#fff;font-family:"Roboto Condensed",sans-serif;font-weight:300;font-size:29px;display:flex;align-items:center;justify-content:center;letter-spacing:.3px}
.card{position:absolute;width:357px;background:#fff;box-shadow:0 0 8px rgba(0,0,0,.12);overflow:hidden}
.card-head{height:45px;display:flex;align-items:center;justify-content:center;color:#fff;font-family:"Russo One",sans-serif;font-size:25px;letter-spacing:1px;position:relative}
.average{background:var(--average)}
.good{background:var(--good)}
.great{background:var(--great)}
.habits{list-style:none;padding:40px 8px 0 78px}
.habits li{position:relative;font-size:16.5px;line-height:20px;margin-bottom:20px}
.habits li:last-child{margin-bottom:0}
.habits.compact{padding-top:12px}
.habits.compact li{margin-bottom:19px}
.habits.compact li:last-child{margin-bottom:0}
.habits li::before{content:"";position:absolute;left:-32px;top:3px;width:13px;height:13px;border:2px solid #555;border-radius:50%;box-sizing:border-box}
.habits li::after{content:"";position:absolute;left:-28px;top:7px;width:5px;height:5px;background:#555;border-radius:50%}
.notch{position:absolute;width:0;height:0;border:8px solid transparent;margin-left:-8px}
.skills{position:absolute;left:0;width:1235px;height:73px;display:flex;color:#fff}
.skill{flex:1;display:flex;align-items:center;justify-content:center;gap:12px;font-weight:700;font-size:19px;line-height:23px;text-transform:uppercase;border-right:2px solid rgba(255,255,255,.8)}
.skill:last-child{border-right:none}
.skill svg{width:34px;height:34px;flex:none}
</style>
</head>
<body>
<div class="stage">
<div class="poster">

  <div class="hero" role="img" aria-label="Arena photo with bright lights over the ice and a female hockey player in jersey number 5 seen from behind, holding a stick and helmet"></div>
  <svg class="hero-title" width="1235" height="663" viewBox="0 0 1235 663" aria-label="Hockey Habits">
    <text x="95" y="355" textLength="820" lengthAdjust="spacingAndGlyphs" font-family="Russo One, sans-serif" font-size="165" fill="#fff" stroke="#c0143c" stroke-width="6" paint-order="stroke">HOCKEY</text>
    <text x="95" y="545" textLength="800" lengthAdjust="spacingAndGlyphs" font-family="Russo One, sans-serif" font-size="165" fill="#fff" stroke="#f08a10" stroke-width="6" paint-order="stroke">HABITS</text>
  </svg>

  <!-- Individual -->
  <div class="tab" style="left:418px;top:596px;width:350px;background:var(--red);font-size:46px">INDIVIDUAL</div>
  <div class="band" style="top:663px;background:var(--red)">WHAT WE WANT EVERY PLAYER TO HAVE REGARDLESS OF THE TEAM SITUATION</div>

  <div class="card" style="left:25px;top:740px;height:375px">
    <div class="card-head average">AVERAGE</div>
    <ul class="habits">
      <li>Watches during games and doesn't<br>work hard in practice</li>
      <li>Gets easily upset with everyone</li>
      <li>ALL-IN when team is winning</li>
      <li>Works hard when they want to</li>
      <li>They should get me the puck</li>
      <li>Thinks they know hockey</li>
    </ul>
  </div>
  <div class="card" style="left:428px;top:740px;height:375px">
    <div class="card-head good">GOOD</div>
    <ul class="habits">
      <li>Competes during games</li>
      <li>Park Mistakes<br>(their's, teammates, referees)</li>
      <li>ALL-IN during all games</li>
      <li>Works as hard as their opponents</li>
      <li>I'll pass if I have to</li>
      <li>Knows that they need to learn</li>
    </ul>
  </div>
  <div class="card" style="left:831px;top:740px;height:375px">
    <div class="card-head great">GREAT</div>
    <ul class="habits">
      <li>Competes during games and practices</li>
      <li>Able to turn negative situations<br>into positive energy and use it!</li>
      <li>ALL-IN during practice and games</li>
      <li>Their effort matches the best of their<br>ability - they give 100% all the time!</li>
      <li>Watches pro, college, youth games<br>trying to always learn</li>
    </ul>
  </div>
  <div class="notch" style="left:206px;top:736px;border-top-color:var(--red)"></div>
  <div class="notch" style="left:609px;top:736px;border-top-color:var(--red)"></div>
  <div class="notch" style="left:1012px;top:736px;border-top-color:var(--red)"></div>

  <div class="skills" style="top:1115px;background:var(--red)">
    <div class="skill"><svg viewBox="0 0 34 34" fill="none" stroke="#fff" stroke-width="3"><path d="M6 28l22-22M10 6l4 4M28 24l-4-4"/></svg>COMPETE</div>
    <div class="skill"><svg viewBox="0 0 34 34" fill="#fff"><path d="M17 3l11 4v9c0 8-5 13-11 15C11 29 6 24 6 16V7z"/></svg>MENTAL<br>TOUGHNESS</div>
    <div class="skill"><svg viewBox="0 0 34 34" fill="#fff"><path d="M17 2c2 7 10 10 10 19a10 10 0 0 1-20 0c0-6 4-8 5-13 2 3 3 4 5-6z"/></svg>SPIRIT</div>
    <div class="skill"><svg viewBox="0 0 34 34" fill="none" stroke="#fff" stroke-width="3"><path d="M4 30h10v-8h8v-8h8"/><circle cx="24" cy="7" r="4"/></svg>EFFORT</div>
    <div class="skill"><svg viewBox="0 0 34 34" fill="#fff"><circle cx="7" cy="9" r="3"/><circle cx="17" cy="7" r="3"/><circle cx="27" cy="9" r="3"/><rect x="4" y="14" width="6" height="16"/><rect x="14" y="12" width="6" height="18"/><rect x="24" y="14" width="6" height="16"/></svg>TEAMWORK</div>
    <div class="skill"><svg viewBox="0 0 34 34" fill="none" stroke="#fff" stroke-width="3"><circle cx="17" cy="14" r="9"/><path d="M13 27h8M14 31h6"/></svg>HOCKEY IQ</div>
  </div>

  <!-- Offense with puck -->
  <div class="tab" style="left:326px;top:1228px;width:539px;background:var(--purple);font-size:44px">OFFENSE W/PUCK</div>
  <div class="band" style="top:1303px;background:var(--purple)">YOU HAVE THE PUCK AND YOUR TEAM IS ON OFFENSE</div>

  <div class="card" style="left:25px;top:1380px;height:373px">
    <div class="card-head average">AVERAGE</div>
    <ul class="habits" style="padding-left:90px">
      <li>Eyes always on the puck</li>
      <li>Control puck in front of body</li>
      <li>Blindly hitting the puck</li>
      <li>Shoots towards the net<br>wherever they are</li>
      <li>Making a deke, pass or shot<br>once D is on you</li>
    </ul>
  </div>
  <div class="card" style="left:428px;top:1380px;height:373px">
    <div class="card-head good">GOOD</div>
    <ul class="habits">
      <li>Eyes on puck see game in<br>peripheral vision</li>
      <li>Control puck side to side</li>
      <li>Making a pass toward teammate</li>
      <li>Shoots hard towards the net</li>
      <li>Making a deke, pass or shot<br>before the D is on you</li>
    </ul>
  </div>
  <div class="card" style="left:831px;top:1380px;height:373px">
    <div class="card-head great">GREAT</div>
    <ul class="habits" style="padding-left:93px">
      <li>Eyes on the game peripheral<br>vision for puck</li>
      <li>Control puck in all positions</li>
      <li>Make a pass with eyes up tape to<br>tape to where the player is going</li>
      <li>Finds a good shooting lane and<br>shoots as hard as they possibly can</li>
      <li>Anticipate the play and play in<br>areas D can't get you</li>
    </ul>
  </div>
  <div class="notch" style="left:206px;top:1376px;border-top-color:var(--purple)"></div>
  <div class="notch" style="left:609px;top:1376px;border-top-color:var(--purple)"></div>
  <div class="notch" style="left:1012px;top:1376px;border-top-color:var(--purple)"></div>

  <div class="skills" style="top:1756px;background:var(--purple)">
    <div class="skill"><svg viewBox="0 0 34 34" fill="none" stroke="#fff" stroke-width="3"><circle cx="22" cy="5" r="3"/><path d="M20 10l-6 8 6 4-2 9M14 18l-8 4M6 30h14"/></svg>SKATING WITH<br>THE PUCK</div>
    <div class="skill"><svg viewBox="0 0 34 34" fill="none" stroke="#fff" stroke-width="3"><path d="M6 6l22 22M28 6L6 28"/><circle cx="17" cy="30" r="2" fill="#fff"/></svg>STICKHANDLING</div>
    <div class="skill"><svg viewBox="0 0 34 34" fill="#fff"><path d="M4 28c2-10 9-15 18-15V7l10 9-10 9v-6c-8 0-13 3-18 9z"/></svg>MAKING A<br>PASS</div>
    <div class="skill"><svg viewBox="0 0 34 34" fill="none" stroke="#fff" stroke-width="3"><path d="M3 10l14 14h6M26 10l6-4M26 16h7"/></svg>SHOOTING</div>
    <div class="skill"><svg viewBox="0 0 34 34" fill="none" stroke="#fff" stroke-width="3"><circle cx="17" cy="27" r="4" fill="#fff"/><path d="M17 21V5M17 5l-4 4M17 5l4 4M11 17L4 12M23 17l7-5"/></svg>PLAY<br>MAKING</div>
  </div>

  <!-- Offense without puck -->
  <div class="tab" style="left:347px;top:1863px;width:580px;background:var(--blue);font-size:44px">OFFENSE W/O/PUCK</div>
  <div class="band" style="top:1936px;background:var(--blue)">YOU DO NOT HAVE THE PUCK BUT YOUR TEAMMATE DOES</div>

  <div class="card" style="left:25px;top:2012px;height:376px">
    <div class="card-head average">AVERAGE</div>
    <ul class="habits" style="padding-left:90px">
      <li>Puck deflects off stick</li>
      <li>Not in a good spot to get a rebound</li>
      <li>Standing still covered</li>
      <li>Out of position</li>
      <li>Playing in an only offensive spot</li>
    </ul>
  </div>
  <div class="card" style="left:428px;top:2012px;height:376px">
    <div class="card-head good">GOOD</div>
    <ul class="habits">
      <li>Puck hits stick but body is in control</li>
      <li>In the area for a rebound</li>
      <li>Standing still in open ice</li>
      <li>In position</li>
      <li>React to play switching to defense</li>
    </ul>
  </div>
  <div class="card" style="left:831px;top:2012px;height:376px">
    <div class="card-head great">GREAT</div>
    <ul class="habits compact" style="padding-left:90px">
      <li>Puck is controlled in a hockey<br>position ready to make hockey play</li>
      <li>In the area, feet positioned properly,<br>stick is on the ice and the player is<br>working hard to get the puck in the net</li>
      <li>Constantly moving to find open ice<br>and passing lanes</li>
      <li>In position but able to adjust<br>to where teammates are</li>
      <li>Read when puck might turn to defense<br>and already be moving to a spot</li>
    </ul>
  </div>
  <div class="notch" style="left:206px;top:2008px;border-top-color:var(--blue)"></div>
  <div class="notch" style="left:609px;top:2008px;border-top-color:var(--blue)"></div>
  <div class="notch" style="left:1012px;top:2008px;border-top-color:var(--blue)"></div>

  <div class="skills" style="top:2388px;background:var(--blue)">
    <div class="skill"><svg viewBox="0 0 34 34" fill="none" stroke="#fff" stroke-width="3"><path d="M3 12l14 12h8"/><circle cx="30" cy="24" r="2" fill="#fff"/></svg>RECEIVING<br>A PASS</div>
    <div class="skill"><svg viewBox="0 0 34 34" fill="#fff"><rect x="2" y="6" width="22" height="16" rx="2"/><rect x="20" y="14" width="12" height="14" rx="2"/><rect x="6" y="24" width="12" height="3"/></svg>REBOUNDS,<br>TIPS, SCREENS</div>
    <div class="skill"><svg viewBox="0 0 34 34" fill="none" stroke="#fff" stroke-width="3"><circle cx="14" cy="14" r="10"/><path d="M21 21l10 10M9 14l4 4 6-7"/></svg>FINDING<br>OPEN ICE</div>
    <div class="skill"><svg viewBox="0 0 34 34" fill="#fff"><circle cx="17" cy="6" r="4"/><rect x="13" y="12" width="8" height="14" rx="2"/><path d="M4 26c0 4 26 4 26 0" fill="none" stroke="#fff" stroke-width="3"/></svg>POSITIONING<br>(TRADITIONAL ROLES)</div>
    <div class="skill"><svg viewBox="0 0 34 34" fill="#fff"><path d="M4 10h18V5l9 8-9 8v-5H4zM30 24H12v-5l-9 8 9 8v-5h18z" transform="scale(.95)"/></svg>READY TO SWITCH<br>TO DEFENSE</div>
  </div>

</div>
</div>
</body>
</html>
```